Brantley Advisory Group provides support for renewable energy projects to utilities and suppliers

I need a professional looking business card that is both simple and elegant and unique. My clients are mostly large organizations not individuals. I am a consultant with my own company that is small but would like to give clients the impression I am larger. Smart grid, fiber optics, software, field hardware, distribution automation, substation automation, operations, energy storage/batteries, microgrids, customer service, strategy/roadmaps, conservation, Automated Metering Infrastruture (AMI or smart meters) are all areas of focus.

Target Market(s)

Utilities, suppliers, governmental agencies involved in energy. All types of energy especially natural gas and electrical. Especially renewable energy or green projects.

Contact Information for Business Card

Name - Mark Brantley Cell Phone - 425.318.2746 Email - mbrantley@brantleyag-example.com
Company - Brantley Advisory Group (logo) Title - Principal

Font styles to use
Serif
Sans Serif

Colors

Designer to choose colors to be used in the design.

Requirements
Must have
• Simple and professional and powerful.
• Unique/creative design.
Nice to have
• Utilize color scheme to accent logo colors. Maybe some geometric pattern on edge of card with color.
Should not have
• Busy, complicated, traditional

```html
<!DOCTYPE html>
<html lang="en">
<head>
<meta charset="utf-8">
<title>Brantley Advisory Group – Business Card</title>
<link rel="stylesheet" href="https://fonts.googleapis.com/css2?family=Open+Sans:wght@300;400;600;700&display=swap">
<style>
  :root {
    --page-bg: #d6d7d9;
    --card-bg: #242526;
    --card-bg-light: #2b2c2e;
    --brand-blue: #2447b0;
    --brand-green: #6a9d38;
    --brand-gray: #a3a3a3;
    --text-light: #c9cacc;
    --text-muted: #a9aaac;
  }
  * { box-sizing: border-box; margin: 0; padding: 0; }
  html, body {
    width: 1200px;
    height: 766px;
    overflow: hidden;
    background: var(--page-bg);
    font-family: "Open Sans", Arial, sans-serif;
  }
  .canvas {
    position: relative;
    width: 1200px;
    height: 766px;
    display: flex;
    align-items: center;
    justify-content: center;
    gap: 50px;
  }
  .card {
    position: relative;
    width: 525px;
    height: 300px;
    border-radius: 14px;
    overflow: hidden;
    background: linear-gradient(135deg, var(--card-bg-light), var(--card-bg));
    box-shadow: 0 10px 24px rgba(0, 0, 0, 0.25);
  }
  .edge-stripe {
    position: absolute;
    left: 0;
    right: 0;
    bottom: 0;
    height: 9px;
    display: flex;
  }
  .edge-stripe .seg-blue { flex: 36; background: var(--brand-blue); }
  .edge-stripe .seg-gray { flex: 33; background: var(--brand-gray); }
  .edge-stripe .seg-green { flex: 31; background: var(--brand-green); }

  .brand {
    display: flex;
    align-items: center;
    gap: 14px;
  }
  .brand-square {
    flex: none;
    border: 3px solid var(--brand-gray);
    border-radius: 4px;
  }
  .brand-name {
    color: var(--brand-green);
    font-weight: 700;
    line-height: 1.1;
  }

  /* Front */
  .card-front .brand {
    position: absolute;
    left: 40px;
    top: 58px;
  }
  .card-front .brand-square { width: 42px; height: 42px; }
  .card-front .brand-name { font-size: 27px; }

  .person {
    position: absolute;
    left: 40px;
    top: 178px;
  }
  .person-name {
    color: var(--brand-blue);
    font-size: 22px;
    font-weight: 400;
    letter-spacing: 0.5px;
    text-transform: uppercase;
  }
  .person-title {
    color: var(--text-muted);
    font-size: 14px;
    font-weight: 400;
    margin-top: 2px;
    margin-left: 70px;
  }
  .divider {
    position: absolute;
    left: 236px;
    top: 172px;
    width: 2px;
    height: 62px;
    background: var(--brand-green);
  }
  .contact {
    position: absolute;
    left: 254px;
    top: 170px;
    list-style: none;
  }
  .contact li {
    display: flex;
    align-items: center;
    gap: 8px;
    color: var(--text-light);
    font-size: 13px;
    font-weight: 300;
    line-height: 22px;
  }
  .contact svg { width: 12px; height: 12px; flex: none; }

  /* Back */
  .card-back .brand {
    position: absolute;
    left: 0;
    right: 0;
    top: 0;
    bottom: 9px;
    justify-content: center;
  }
  .card-back .brand-square { width: 54px; height: 54px; }
  .card-back .brand-name { font-size: 33px; }
</style>
</head>
<body>
<main class="canvas">
  <section class="card card-front">
    <div class="brand">
      <span class="brand-square"></span>
      <span class="brand-name">Brantley Advisory Group</span>
    </div>

    <div class="person">
      <p class="person-name">Mark Brantley</p>
      <p class="person-title">Principal</p>
    </div>

    <span class="divider"></span>

    <ul class="contact">
      <li>
        <svg viewBox="0 0 24 24" fill="var(--brand-blue)" aria-hidden="true"><path d="M6.6 10.8a15.1 15.1 0 0 0 6.6 6.6l2.2-2.2c.3-.3.7-.4 1-.2 1.1.4 2.3.6 3.6.6.6 0 1 .4 1 1V20c0 .6-.4 1-1 1C10.6 21 3 13.4 3 4c0-.6.4-1 1-1h3.5c.6 0 1 .4 1 1 0 1.3.2 2.5.6 3.6.1.3 0 .7-.2 1z"/></svg>
        425.318.2746
      </li>
      <li>
        <svg viewBox="0 0 24 24" fill="var(--brand-blue)" aria-hidden="true"><path d="M2 5h20v14H2z"/><path d="M2 5l10 8 10-8" fill="none" stroke="#242526" stroke-width="2"/></svg>
        mbrantley@brantleyag-example.com
      </li>
      <li>
        <svg viewBox="0 0 24 24" fill="none" stroke="var(--brand-blue)" stroke-width="2.4" aria-hidden="true"><circle cx="12" cy="12" r="10"/><path d="M2 12h20M12 2c3 3 3 17 0 20M12 2c-3 3-3 17 0 20"/></svg>
        www.brantleyag-example.com
      </li>
    </ul>

    <div class="edge-stripe">
      <span class="seg-blue"></span><span class="seg-gray"></span><span class="seg-green"></span>
    </div>
  </section>

  <section class="card card-back">
    <div class="brand">
      <span class="brand-square"></span>
      <span class="brand-name">Brantley Advisory Group</span>
    </div>

    <div class="edge-stripe">
      <span class="seg-blue"></span><span class="seg-gray"></span><span class="seg-green"></span>
    </div>
  </section>
</main>
</body>
</html>
```